TREMLUX electrical and air conditioning

the van(KMR vantrek 5 LWB in Australia) wrap design features a dynamic and eye-catching layout that enhances brand visibility while reflecting our core values and mission.
A vibrant color scheme, captures attention and evokes emotions associated with our brand. The colors are strategically placed to create a sense of movement and energy.Graphics: Bold, high-resolution graphics highlight our key services, which are refrigeration and electrical.

Target Market(s)

Locals

Requirements
Must have
• services including : Electrical/air conditioning / refrigeration / data

```html
<!DOCTYPE html>
<html lang="en">
<head>
<meta charset="utf-8">
<title>TREMLUX van wrap</title>
<link href="https://fonts.googleapis.com/css2?family=Russo+One&family=Saira+Condensed:wght@600;800&display=swap" rel="stylesheet">
<style>
  :root {
    --bg: #f3f3f3;
    --wrap-dark: #262626;
    --wrap-white: #f7f7f7;
    --orange: #f07a12;
    --amber: #f7b21c;
    --blue: #3aa6e0;
    --steel: #c9c9c9;
    --ink: #111111;
    --rule: #9a9a9a;
  }
  * { box-sizing: border-box; margin: 0; padding: 0; }
  html, body { width: 1124px; height: 1200px; overflow: hidden; background: var(--bg); }
  body { position: relative; font-family: "Saira Condensed", sans-serif; }

  .panel { position: absolute; overflow: hidden; border-radius: 18px; background: var(--wrap-dark); }

  .side-panel { left: 32px; top: 40px; width: 1060px; height: 470px; }
  .rear-panel { left: 282px; top: 580px; width: 560px; height: 580px; }

  .service-field { position: absolute; background: var(--wrap-white); }
  .side-panel .service-field { left: 470px; top: 0; width: 590px; height: 250px; border-bottom-left-radius: 40px; }
  .rear-panel .service-field { left: 0; top: 310px; width: 560px; height: 270px; }

  .accent-band { position: absolute; background: linear-gradient(90deg, var(--orange), var(--amber) 55%, var(--blue)); }
  .side-panel .accent-band { left: 370px; top: 264px; width: 690px; height: 46px; border-radius: 23px 0 0 23px; }
  .rear-panel .accent-band { left: 0; top: 278px; width: 560px; height: 26px; }

  .brand { position: absolute; text-align: center; }
  .brand-est { display: flex; justify-content: space-between; font-weight: 600; font-size: 12px; color: #d9d9d9; letter-spacing: 1px; }
  .brand-name { display: flex; align-items: center; justify-content: center; gap: 10px; font-family: "Russo One", sans-serif; color: var(--blue); line-height: 1; }
  .brand-dot { width: 14px; height: 14px; border-radius: 50%; background: var(--orange); }
  .brand-tag { font-weight: 600; color: #e6e6e6; letter-spacing: 1.5px; margin-top: 6px; }

  .side-panel .brand { left: 70px; top: 110px; width: 320px; }
  .side-panel .brand-name { font-size: 52px; }
  .side-panel .brand-tag { font-size: 13px; }

  .web-pill { position: absolute; background: var(--orange); color: #fff3e0; font-family: "Russo One", sans-serif; border-radius: 20px; text-align: center; letter-spacing: 1px; }
  .side-panel .web-pill { left: 110px; top: 250px; width: 230px; height: 36px; line-height: 36px; font-size: 15px; }

  .services { position: absolute; list-style: none; }
  .services li { display: flex; align-items: center; gap: 14px; font-weight: 800; color: var(--ink); text-transform: uppercase; border-bottom: 1px dotted var(--rule); }
  .services li:last-child { border-bottom: none; }
  .svc-icon { flex: none; border-radius: 50%; background: var(--ink); display: flex; align-items: center; justify-content: center; }
  .svc-icon svg { width: 60%; height: 60%; }

  .side-panel .services { left: 510px; top: 26px; width: 330px; }
  .side-panel .services li { height: 52px; font-size: 24px; }
  .side-panel .svc-icon { width: 30px; height: 30px; }

  .phone { position: absolute; font-family: "Russo One", sans-serif; letter-spacing: 3px; white-space: nowrap; }
  .side-panel .phone { left: 380px; top: 335px; font-size: 66px; color: var(--steel); -webkit-text-stroke: 2px #0a0a0a; text-shadow: 3px 3px 0 #000; }

  .rear-panel .brand { left: 110px; top: 60px; width: 340px; }
  .rear-panel .brand-name { font-size: 54px; }
  .rear-panel .brand-tag { font-size: 13px; }
  .rear-panel .services { left: 22px; top: 330px; width: 200px; }
  .rear-panel .services li { height: 52px; font-size: 21px; gap: 10px; }
  .rear-panel .svc-icon { width: 26px; height: 26px; }
  .rear-panel .phone { left: 250px; top: 450px; font-size: 38px; color: var(--orange); letter-spacing: 1px; }
  .rear-web { position: absolute; left: 268px; top: 506px; font-family: "Russo One", sans-serif; font-size: 17px; color: var(--ink); letter-spacing: 1px; }
</style>
</head>
<body>

<section class="panel side-panel" aria-label="Van side wrap">
  <div class="service-field"></div>
  <div class="accent-band" role="img" aria-label="Decorative orange, amber and blue wave band"></div>

  <div class="brand">
    <div class="brand-est"><span>ESTD.</span><span>2020</span></div>
    <div class="brand-name"><span class="brand-dot"></span>TREMLUX</div>
    <div class="brand-tag">ELECTRICAL&amp;AIR CONDITIONING</div>
  </div>

  <div class="web-pill">WWW.TREMLUXCO.COM</div>

  <ul class="services">
    <li><span class="svc-icon"><svg viewBox="0 0 20 20"><rect x="3" y="4" width="14" height="9" fill="none" stroke="var(--orange)" stroke-width="2"/><path d="M7 16h6" stroke="var(--orange)" stroke-width="2"/></svg></span>Data</li>
    <li><span class="svc-icon"><svg viewBox="0 0 20 20"><path d="M11 2 5 11h4l-1 7 6-10h-4z" fill="var(--orange)"/></svg></span>Electrical</li>
    <li><span class="svc-icon"><svg viewBox="0 0 20 20"><rect x="5" y="2" width="10" height="16" fill="none" stroke="var(--orange)" stroke-width="2"/><path d="M5 8h10" stroke="var(--orange)" stroke-width="2"/></svg></span>Refrigeration</li>
    <li><span class="svc-icon"><svg viewBox="0 0 20 20"><rect x="2" y="5" width="16" height="7" fill="none" stroke="var(--orange)" stroke-width="2"/><path d="M6 15v2M10 15v2M14 15v2" stroke="var(--orange)" stroke-width="2"/></svg></span>Air Conditioning</li>
  </ul>

  <div class="phone">0400 555 019</div>
</section>

<section class="panel rear-panel" aria-label="Van rear wrap">
  <div class="service-field"></div>
  <div class="accent-band" role="img" aria-label="Decorative orange, amber and blue wave band"></div>

  <div class="brand">
    <div class="brand-est"><span>ESTD.</span><span>2020</span></div>
    <div class="brand-name"><span class="brand-dot"></span>TREMLUX</div>
    <div class="brand-tag">ELECTRICAL&amp;AIR CONDITIONING</div>
  </div>

  <ul class="services">
    <li><span class="svc-icon"><svg viewBox="0 0 20 20"><rect x="3" y="4" width="14" height="9" fill="none" stroke="var(--orange)" stroke-width="2"/><path d="M7 16h6" stroke="var(--orange)" stroke-width="2"/></svg></span>Data</li>
    <li><span class="svc-icon"><svg viewBox="0 0 20 20"><path d="M11 2 5 11h4l-1 7 6-10h-4z" fill="var(--orange)"/></svg></span>Electrical</li>
    <li><span class="svc-icon"><svg viewBox="0 0 20 20"><rect x="5" y="2" width="10" height="16" fill="none" stroke="var(--orange)" stroke-width="2"/><path d="M5 8h10" stroke="var(--orange)" stroke-width="2"/></svg></span>Refrigeration</li>
    <li><span class="svc-icon"><svg viewBox="0 0 20 20"><rect x="2" y="5" width="16" height="7" fill="none" stroke="var(--orange)" stroke-width="2"/><path d="M6 15v2M10 15v2M14 15v2" stroke="var(--orange)" stroke-width="2"/></svg></span>Air Conditioning</li>
  </ul>

  <div class="phone">0400 555 019</div>
  <div class="rear-web">WWW.TREMLUXCO.COM</div>
</section>

</body>
</html>
```